Business Card Design - Carrington Hill Lodge

We are looking at a new design for our business cards that has a modern and professional look. We run a residential aged care facility focussing on the care of residents. The cards will be used for potential clients, consultants and business opportunities in this sector. Blue and white is our main colours and would to see these colours incorporated in the design.
Industry/Entity Type
Business
Contact Information for Business Card
Carrington Hill Lodge, Darren Pelham, dpelham@carringtonhilllodge.com.au, Finance Manager, 0491 736 208, BCom, 48 Yarrabee Way, Marlowe Park, Qld 4306.

```html
<!DOCTYPE html>
<html lang="en">
<head>
<meta charset="utf-8">
<title>Carrington Hill Lodge – Business Card</title>
<link rel="stylesheet" href="https://fonts.googleapis.com/css2?family=Josefin+Sans:wght@400;600&display=swap">
<style>
  :root {
    --navy: #143d58;
    --red-rule: #b21f2a;
    --cyan-rule: #3fd8e8;
    --card-text: #e8f0f4;
    --logo-ground: #e1f0f5;
    --logo-ink: #1f4d69;
    --logo-dot: #3f8eab;
    --gap: #ffffff;
  }
  html, body {
    margin: 0;
    padding: 0;
    width: 1200px;
    height: 368px;
    overflow: hidden;
    background: var(--gap);
    font-family: "Josefin Sans", sans-serif;
  }
  .card {
    position: absolute;
    top: 0;
    width: 595px;
    height: 368px;
    background: var(--navy);
    color: var(--card-text);
  }
  .card--front { left: 0; }
  .card--back { left: 605px; }
  .card__rule {
    position: absolute;
    box-sizing: border-box;
  }
  .card__rule--outer { inset: 9px; border: 2px solid var(--red-rule); }
  .card__rule--inner { inset: 21px; border: 2px solid var(--cyan-rule); }

  .logo-frame {
    position: absolute;
    box-sizing: border-box;
    border: 1.5px solid var(--cyan-rule);
  }
  .logo-frame__ground {
    position: absolute;
    background: var(--logo-ground);
    display: flex;
    flex-direction: column;
    align-items: center;
    justify-content: center;
    text-align: center;
    color: var(--logo-ink);
    font-weight: 600;
    text-transform: uppercase;
    letter-spacing: 0.06em;
    line-height: 1.15;
  }
  .logo-frame__dot {
    border-radius: 50%;
    background: var(--logo-dot);
  }
  .card--front .logo-frame { left: 163px; top: 61px; width: 278px; height: 207px; }
  .card--front .logo-frame__ground { inset: 9px; font-size: 27px; gap: 16px; }
  .card--front .logo-frame__dot { width: 34px; height: 34px; }
  .card--back .logo-frame { left: 50px; top: 41px; width: 143px; height: 106px; }
  .card--back .logo-frame__ground { inset: 5px; font-size: 13px; gap: 8px; }
  .card--back .logo-frame__dot { width: 16px; height: 16px; }

  .role {
    position: absolute;
    margin: 0;
    font-size: 18px;
    font-variant: small-caps;
    line-height: 24px;
  }
  .card--front .role { left: 163px; width: 278px; top: 272px; text-align: center; }
  .card--back .role { left: 0; width: 193px; top: 157px; text-align: right; font-size: 17px; }

  .phone {
    position: absolute;
    left: 388px;
    top: 36px;
    margin: 0;
    font-size: 18px;
    letter-spacing: 0.12em;
  }
  .address {
    position: absolute;
    left: 262px;
    top: 178px;
    margin: 0;
    font-style: normal;
    font-size: 15px;
    line-height: 30px;
    font-variant: small-caps;
    white-space: nowrap;
  }
  .address__email { font-variant: normal; }
</style>
</head>
<body>
  <section class="card card--front">
    <div class="card__rule card__rule--outer"></div>
    <div class="card__rule card__rule--inner"></div>
    <div class="logo-frame">
      <div class="logo-frame__ground">
        <span class="logo-frame__dot"></span>
        <span class="logo-frame__name">Carrington Hill<br>Lodge</span>
      </div>
    </div>
    <p class="role">Finance Manager<br>BCom</p>
  </section>

  <section class="card card--back">
    <div class="card__rule card__rule--outer"></div>
    <div class="card__rule card__rule--inner"></div>
    <div class="logo-frame">
      <div class="logo-frame__ground">
        <span class="logo-frame__dot"></span>
        <span class="logo-frame__name">Carrington Hill<br>Lodge</span>
      </div>
    </div>
    <p class="role">Finance Manager<br>BCom</p>
    <p class="phone">0491 736 208</p>
    <address class="address">
      48 Yarrabee Way<br>
      Carrington Hill Lodge, Darren Pelham,<br>
      <span class="address__email">dpelham@carringtonhilllodge.com.au</span><br>
      Marlowe Park, Qld 4306
    </address>
  </section>
</body>
</html>
```